Business Card Design - Law Firm

I need a business card design. I have attached a picture of the law firm's website and logo. The business card design should be consistent with those pictures. There should be a place for the employee name, employee job title, telephone number, facsimile number, address, website url, and email address for each employee.
Industry/Entity Type
Business

```html
<!DOCTYPE html>
<html lang="en">
<head>
<meta charset="utf-8">
<title>Ashworth Law – Business Cards</title>
<link rel="stylesheet" href="https://fonts.googleapis.com/css2?family=Cormorant+Garamond:wght@500&family=Open+Sans:wght@400&display=swap">
<style>
  :root {
    --backdrop: #6b6b6c;
    --card-gold: #b3a45c;
    --ink: #3b2f16;
    --ink-soft: #4a3d22;
    --mark: #231c10;
    --tab: #2e2e30;
  }
  * { margin: 0; padding: 0; box-sizing: border-box; }
  html, body {
    width: 1200px; height: 899px; overflow: hidden;
    background: var(--backdrop);
  }
  .canvas { position: relative; width: 1200px; height: 899px; }

  .card {
    position: absolute;
    width: 560px; height: 330px;
    background: var(--card-gold);
    border-radius: 22px;
    color: var(--ink);
    font-family: "Open Sans", Arial, sans-serif;
  }
  .card--front { left: 70px; top: 90px; }
  .card--back  { left: 570px; top: 480px; }

  .brand { position: absolute; display: flex; align-items: center; gap: 16px; }
  .brand__square { background: var(--mark); flex: none; }
  .brand__name {
    font-family: "Cormorant Garamond", Georgia, serif;
    font-weight: 500;
    color: var(--ink-soft);
    white-space: nowrap;
  }
  .card--front .brand { left: 34px; top: 38px; }
  .card--front .brand__square { width: 42px; height: 42px; }
  .card--front .brand__name { font-size: 38px; }

  .card--back .brand { left: 70px; top: 132px; }
  .card--back .brand__square { width: 62px; height: 62px; }
  .card--back .brand__name { font-size: 52px; }

  .holder { position: absolute; right: 34px; top: 44px; text-align: right; }
  .holder__name {
    font-family: "Cormorant Garamond", Georgia, serif;
    font-weight: 500; font-size: 30px; letter-spacing: 1px; line-height: 1;
  }
  .holder__title { font-size: 16px; margin-top: 4px; }

  .address {
    position: absolute; left: 34px; top: 150px;
    font-size: 14px; line-height: 30px;
  }
  .contact {
    position: absolute; right: 44px; top: 150px;
    font-size: 13px; line-height: 30px; text-align: right;
  }
  .website {
    position: absolute; left: 0; right: 0; bottom: 22px;
    text-align: center; font-size: 15px;
  }

  .tabs { position: absolute; right: -8px; top: 158px; width: 24px; height: 80px; }
</style>
</head>
<body>
<main class="canvas">

  <section class="card card--front" aria-label="Business card front">
    <div class="brand">
      <span class="brand__square"></span>
      <span class="brand__name">Ashworth Law</span>
    </div>

    <div class="holder">
      <p class="holder__name">YOUR NAME</p>
      <p class="holder__title">Job Title</p>
    </div>

    <address class="address" style="font-style: normal;">
      48 Linford Lane,<br>
      Suite 310 Dalton,<br>
      Vermont 4417.
    </address>

    <div class="contact">
      <p>T : 123.456.7890</p>
      <p>F : 123.456.7890</p>
      <p>E : 123@ashworthlaw.com</p>
    </div>

    <svg class="tabs" viewBox="0 0 24 80" aria-hidden="true">
      <rect x="4" y="2" width="20" height="14" rx="7" fill="var(--tab)"/>
      <rect x="4" y="32" width="20" height="14" rx="7" fill="var(--tab)"/>
      <rect x="4" y="62" width="20" height="14" rx="7" fill="var(--tab)"/>
    </svg>

    <p class="website">www.ashworthlaw.com</p>
  </section>

  <section class="card card--back" aria-label="Business card back">
    <div class="brand">
      <span class="brand__square"></span>
      <span class="brand__name">Ashworth Law</span>
    </div>
  </section>

</main>
</body>
</html>
```